Children's book business card contest - The more bright colors the better

Hello

PLEASE incorporate THE CHARACTERS ILLUSTRATIONS on the most recent uploaded attachment on the business card.

I'm in the process of completing my first manuscript for my children's book series TiKi TELLS a series of stories from a blended family.

My illustrator and I just completed our logo which you will find attached. Additionally you will find my first idea for my business card which I took from Cardwellio just says it means to get started but I really like the color schema. I will be getting my business card out to editors, agents, teachers, and anyone in the children's book realm. The card needs to be bright, friendly and inviting. It needs to remind you of children I do want a double sided card but I am very open as far as design layout. Below is a description of the book series and how the series will go to give you motivation or ideas. Please only submit injuries worthy of national recognition as the business cards will be passed out across the country to some of the top writing professionals in the industry at a childrens writing conference I will be attending.

Like I mentioned previously please review the information below as it gives you background too much children's book series. I look forward to working with my designer and I look forward to the submissions.

"I'm looking for someone with experience in illustrating children's books and is also passionate about this specific illustration type. My book series will be a series of short stories from a blended family. Each book well always have the same characters but the storyline will be different. Additionally, I'm looking for someone who has experience in taking real life photos and creating real like cartoon illustrations. My children's book series idea is based off of my family and I want us to be the characters. Also, if you have a writing background and could help me with editing that would be a very big plus as well. One of the niches for my children's book series is that my blended family is also blended because of ethnicity. My children's book series will bring light to multiculturalism in families and the different diversities blended families go through. This is an untapped industry in the children's book market. If you have experience with grant writing I am very interested in that as well. Please feel free to respond to any of my needs that you feel you are applicable for. I know I've created an idea that will revolutionize how parents and children read and learn together. My book series idea is innovative, fun and has tremendous crossover ability. Please only reply if you are seriously interested and have current availability. I'm ready to be GREAT and I hope you don't pass on the opportunity to join me! "

Please note: I will be using Cardwellio for my business card ordering so please constructive business card to fit those parameters. Additionally there are three attachments I provided one of them is the actual logo, the other is the almost completed book cover, and the other one is my current business cards from Cardwellio that I am looking to replace.

Target Market(s)

Children and Writing Professionals

Industry/Entity Type

Business

Contact Information for Business Card

I would like this business card to be very colorful. The card needs to attract business writing professionals as well as appeal to children and teachers inside the schooling network

Font styles to use
Serif
Sans Serif

Requirements
Must have
• A lot of color, characteristic, informative and must have all of my contact information
Nice to have
• Originality

```html
<!DOCTYPE html>
<html lang="en">
<head>
<meta charset="utf-8">
<title>TiKi TELLS – Business Card</title>
<link rel="stylesheet" href="https://fonts.googleapis.com/css2?family=Short+Stack&display=swap">
<style>
  :root {
    --page-bg: #e9e7e4;
    --card-base: #f3f0ec;
    --card-edge: #d9d4ce;
    --red-deep: #d8101c;
    --red-main: #e61f2b;
    --red-soft: #f05a64;
    --pink-bubble: #f4a0a6;
    --pink-light: #f8c4c8;
    --cream: #f6e8dc;
    --text-light: #fbeee6;
    --logo-ink: #b80d18;
    --art-top: #b9b6c9;
    --art-bottom: #5a5f8c;
  }
  * { box-sizing: border-box; margin: 0; padding: 0; }
  html, body {
    width: 1200px; height: 970px; overflow: hidden;
    background: var(--page-bg);
    font-family: "Short Stack", "Comic Sans MS", cursive;
  }
  .business-card {
    position: absolute; left: 100px; top: 199px;
    width: 1000px; height: 572px;
    background: linear-gradient(160deg, #f8f6f3, var(--card-base));
    border: 1px solid var(--card-edge);
    border-radius: 8px;
    overflow: hidden;
    box-shadow: 0 10px 30px rgba(0,0,0,.12);
  }
  .card-shapes { position: absolute; inset: 0; width: 100%; height: 100%; }
  .family-artwork {
    position: absolute; left: 50px; top: 56px;
    width: 330px; height: 480px;
    border-radius: 140px 140px 20px 20px;
    background: linear-gradient(180deg, var(--art-top), var(--art-bottom));
    opacity: .85;
  }
  .owner-name {
    position: absolute; right: 58px; top: 52px;
    font-size: 46px; color: var(--text-light); letter-spacing: 1px;
  }
  .owner-title {
    position: absolute; right: 58px; top: 112px;
    font-size: 28px; color: var(--text-light);
  }
  .brand-name {
    position: absolute; left: 352px; top: 215px; width: 260px;
    font-size: 58px; line-height: 1.05; color: var(--logo-ink);
    text-align: center;
  }
  .contact-list {
    position: absolute; left: 700px; top: 236px;
    list-style: none; color: var(--text-light);
  }
  .contact-item {
    display: flex; align-items: center; gap: 14px;
    font-size: 17px; margin-bottom: 14px;
  }
  .contact-item svg { flex: none; }
  .contact-item.phone { font-size: 31px; }
  .contact-item.social span { line-height: 1.15; }
  .tagline {
    position: absolute; right: 58px; top: 510px;
    font-size: 16px; color: var(--cream);
  }
</style>
</head>
<body>
<div class="business-card">
  <svg class="card-shapes" viewBox="0 0 1000 572" aria-hidden="true">
    <path fill="var(--red-main)" d="M392,0 H1000 V572 H376 C360,520 420,500 470,480 C380,470 330,420 330,330 C330,230 380,170 440,150 C390,110 380,50 392,0Z"/>
    <path fill="var(--red-deep)" d="M392,0 H760 C740,60 700,110 610,140 C540,160 470,150 430,120 C392,90 384,40 392,0Z" opacity=".7"/>
    <path fill="var(--pink-bubble)" d="M440,150 C520,120 610,140 650,200 C690,260 680,360 640,420 C600,480 500,490 430,460 C350,430 320,340 340,260 C352,210 390,168 440,150Z" opacity=".9"/>
    <path fill="var(--red-soft)" d="M640,200 C720,165 900,160 1000,175 V440 C900,455 740,455 660,430 C620,360 630,260 640,200Z" opacity=".85"/>
    <path fill="none" stroke="var(--cream)" stroke-width="7" stroke-linecap="round" d="M560,165 C600,188 660,188 700,175"/>
    <path fill="none" stroke="var(--cream)" stroke-width="6" stroke-linecap="round" d="M380,210 C400,180 440,165 470,165"/>
    <path fill="none" stroke="var(--cream)" stroke-width="6" stroke-linecap="round" d="M690,205 C740,192 790,188 830,190"/>
    <path fill="none" stroke="var(--cream)" stroke-width="7" stroke-linecap="round" d="M590,478 C630,468 690,466 720,472"/>
  </svg>

  <div class="family-artwork" role="img" aria-label="Illustration of the family characters: father, mother, son and their small brown dog"></div>

  <h1 class="owner-name">Marisol Bennett</h1>
  <p class="owner-title">Author/Founder</p>

  <p class="brand-name">TiKi TELLS</p>

  <ul class="contact-list">
    <li class="contact-item email">
      <svg width="22" height="16" viewBox="0 0 22 16"><rect x="1" y="1" width="20" height="14" rx="1" fill="none" stroke="var(--text-light)" stroke-width="2"/><path d="M1,1 L11,9 L21,1" fill="none" stroke="var(--text-light)" stroke-width="2"/></svg>
      <span>marisol@tikitells.xyz</span>
    </li>
    <li class="contact-item phone">
      <svg width="16" height="28" viewBox="0 0 16 28"><rect x="1" y="1" width="14" height="26" rx="3" fill="none" stroke="var(--text-light)" stroke-width="2"/><circle cx="8" cy="22" r="1.6" fill="var(--text-light)"/></svg>
      <span>555.204.7731</span>
    </li>
    <li class="contact-item social">
      <svg width="22" height="22" viewBox="0 0 22 22"><circle cx="11" cy="11" r="9" fill="var(--text-light)"/></svg>
      <span>Follow me on Chirper<br>@tiki_tells_xyz</span>
    </li>
    <li class="contact-item web">
      <svg width="22" height="22" viewBox="0 0 22 22" fill="none" stroke="var(--text-light)" stroke-width="1.6"><circle cx="11" cy="11" r="9"/><ellipse cx="11" cy="11" rx="4" ry="9"/><path d="M2,11 H20 M4,6 H18 M4,16 H18"/></svg>
      <span>www.tikitells.xyz</span>
    </li>
  </ul>

  <p class="tagline">A series of short stories from a Blended family</p>
</div>
</body>
</html>
```